Kestrel Photography Business Card

I need a business card designed for a photography business based in Perth, Western Australia called Kestrel Photography.

We specialise in wedding, event photography and portrait photography.

The business card must borrow the style of the attached logo.

The hex codes for the colours in the logo are:
#ED1D85 - Pink
#89C23E - Green
#37282F - Black

The name on the card will be:
Name: Toviran
Phone: 0417395268
Website: www.kestrelphotography.com.au
Facebook: kestrelphotography

I am open and happy to accept creative concepts.

I’d like some space at the back for writing notes and appointment details.

```html
<!DOCTYPE html>
<html lang="en">
<head>
<meta charset="utf-8">
<title>Kestrel Photography – Business Card</title>
<link href="https://fonts.googleapis.com/css2?family=Advent+Pro:wght@400&family=Didact+Gothic&family=PT+Sans:wght@400;700&display=swap" rel="stylesheet">
<style>
  :root {
    --pink: #ED1D85;
    --green: #89C23E;
    --ink: #37282F;
    --paper: #ffffff;
    --backdrop: #e9e7e4;
    --rule: #222;
  }
  * { margin: 0; padding: 0; box-sizing: border-box; }
  html, body {
    width: 1200px; height: 984px; overflow: hidden;
    background: var(--backdrop);
  }
  .card {
    position: absolute; left: 220px;
    width: 760px; height: 446px;
    background: var(--paper);
    overflow: hidden;
    box-shadow: 0 4px 14px rgba(0,0,0,.18);
  }
  .card--back { top: 26px; }
  .card--front { top: 510px; }
  .card__bands { position: absolute; inset: 0; width: 100%; height: 100%; }
  .band-pink { fill: var(--pink); }
  .band-green { fill: var(--green); }

  .brand-mark {
    position: absolute; width: 80px; height: 80px;
    border-radius: 50%; background: var(--pink);
  }
  .wordmark {
    position: absolute;
    font-family: "Didact Gothic", sans-serif;
    font-size: 15px; letter-spacing: 7px;
    color: var(--ink); text-transform: uppercase; white-space: nowrap;
  }

  /* back */
  .card--back .brand-mark { left: 340px; top: 26px; }
  .card--back .wordmark { left: 0; right: 0; top: 124px; text-align: center; }
  .notes-line {
    position: absolute; left: 90px; width: 600px; height: 0;
    border-top: 1.5px solid var(--rule);
  }
  .notes-line--1 { top: 212px; }
  .notes-line--2 { top: 276px; }

  /* front */
  .web-tab {
    position: absolute; left: 30px; top: 16px;
    font-family: "PT Sans", sans-serif; font-weight: 700;
    font-size: 16px; color: var(--paper);
  }
  .card--front .brand-mark { left: 495px; top: 28px; }
  .card--front .wordmark { right: 36px; top: 124px; }
  .person__name {
    position: absolute; left: 487px; top: 196px;
    font-family: "Advent Pro", sans-serif; font-size: 40px;
    color: #111; letter-spacing: -0.5px;
  }
  .person__role {
    position: absolute; left: 487px; top: 244px;
    font-family: "PT Sans", sans-serif; font-size: 15px; color: #333;
  }
  .contact {
    position: absolute; left: 36px; top: 310px;
    font-family: "PT Sans", sans-serif; font-size: 15px; color: #111;
    list-style: none;
  }
  .contact__row { display: flex; align-items: center; height: 22px; white-space: nowrap; }
  .contact__item { display: inline-flex; align-items: center; }
  .contact__item + .contact__item { margin-left: 28px; }
  .icon { width: 13px; height: 13px; margin-right: 5px; fill: var(--pink); flex: none; }
  .icon--mail { width: 20px; }
  .social-square { width: 12px; height: 12px; background: var(--pink); margin-right: 5px; }
</style>
</head>
<body>

<section class="card card--back" aria-label="Card back with notes space">
  <svg class="card__bands" viewBox="0 0 760 446" preserveAspectRatio="none" aria-hidden="true">
    <rect class="band-pink" x="0" y="0" width="760" height="12"/>
    <path class="band-green" d="M0 378 C180 366 420 360 540 356 C600 354 615 310 660 300 C690 294 720 290 760 288 V446 H0 Z"/>
  </svg>
  <div class="brand-mark" aria-hidden="true"></div>
  <p class="wordmark">Kestrel Photography</p>
  <div class="notes-line notes-line--1"></div>
  <div class="notes-line notes-line--2"></div>
</section>

<section class="card card--front" aria-label="Card front with contact details">
  <svg class="card__bands" viewBox="0 0 760 446" preserveAspectRatio="none" aria-hidden="true">
    <rect class="band-pink" x="300" y="0" width="460" height="16"/>
    <path class="band-green" d="M0 0 H335 C300 2 300 50 262 52 H0 Z"/>
    <path class="band-pink" d="M0 372 H470 C495 372 505 380 512 390 H0 Z"/>
    <path class="band-green" d="M0 388 H500 C560 388 560 320 625 318 H760 V446 H0 Z"/>
  </svg>
  <p class="web-tab">www.kestrelphotography.com.au</p>

  <div class="brand-mark" aria-hidden="true"></div>
  <p class="wordmark">Kestrel Photography</p>

  <h1 class="person__name">Toviran</h1>
  <p class="person__role">CEO &amp; Founder</p>

  <ul class="contact">
    <li class="contact__row">
      <svg class="icon" viewBox="0 0 12 16" aria-hidden="true"><path d="M6 0a6 6 0 0 0-6 6c0 4.5 6 10 6 10s6-5.5 6-10a6 6 0 0 0-6-6zm0 8.5A2.5 2.5 0 1 1 6 3.5a2.5 2.5 0 0 1 0 5z"/></svg>
      Unit 4, 18 Harbour Lane, Northbridge, Perth WA
    </li>
    <li class="contact__row">
      <span class="contact__item">
        <svg class="icon" viewBox="0 0 16 16" aria-hidden="true"><path d="M3.6 1 6 3.6 4.6 5.6c.9 2.2 3.6 4.9 5.8 5.8l2-1.4L15 12.4 13.4 15C6.6 15 1 9.4 1 2.6z"/></svg>
        0417395268
      </span>
      <span class="contact__item">
        <svg class="icon icon--mail" viewBox="0 0 20 13" aria-hidden="true"><path d="M0 0h20v13H0z M1.5 1.5 10 8l8.5-6.5" fill="none" stroke="var(--pink)" stroke-width="1.6"/></svg>
        www.kestrelphotography.com.au
      </span>
    </li>
    <li class="contact__row">
      <span class="social-square" aria-hidden="true"></span>
      kestrelphotography
    </li>
  </ul>
</section>

</body>
</html>
```